We're a trash valet service. We collect trash that tenants at apartment communitys, elder/assisted liveing would be ideal but we collect Sunday through Thursdays and also offer morning check ups to make sure nothing is left out for pickup. Id like it basic but elegant with little to no cartoon caricatures. But not aposed to them if done right. Colors tequise, orange, blue not married to any of the in spasific.

Lanternway Hauling
Number : 555-314-7290
Address: 438 Quarry Ridge Road SUITE
Millbrook NJ 08000
Email: Marla@lanternway-hauling.example

I attached my logo.
Those don't have to be the colors plain black is fine for the broshour but I do like those colors with orange maybe.
Updates

Everyone is doing such amazing work. I wanted to just make sure I let everyone know what I need and what should not be on broshour. We do not have garbage trucks, we just both of trash in on site dumpsters or compactors. We use tall kitchen cans for residents to put their garbage in and on in the cans outside of their doors. Pictures of hallways with cans with our logo on it would be good definitely no one's face. What we provide for managers and their benefiting from our service. residents expierance. We also don't have a QR code scanner. And the morning check up is an added service.

Target Market(s)

Apartment communitys

Requirements
Should not have
• Garbage trucks

```html
<!DOCTYPE html>
<html lang="en">
<head>
<meta charset="utf-8">
<title>Lanternway Hauling – Valet Trash Service Brochure</title>
<link href="https://fonts.googleapis.com/css2?family=Nunito+Sans:wght@400;600;700;800&family=Source+Serif+4:wght@500;600&display=swap" rel="stylesheet">
<style>
  :root{
    --navy:#0b2545;
    --navy-deep:#08203d;
    --teal:#1c8fa8;
    --teal-light:#33b3cc;
    --teal-band:#1f7f95;
    --orange:#ee8420;
    --ink:#1d2b3f;
    --paper:#ffffff;
    --backdrop:#ececec;
  }
  *{box-sizing:border-box;margin:0;padding:0}
  html,body{width:1200px;height:900px;overflow:hidden;background:var(--backdrop)}
  body{position:relative;font-family:"Nunito Sans",sans-serif;color:var(--ink)}
  .sheet{position:absolute;left:57px;width:1086px;display:flex;background:var(--paper)}
  .sheet--outside{top:12px;height:440px}
  .sheet--inside{top:464px;height:424px}
  .panel{position:relative;height:100%;overflow:hidden}
  .panel--navy{background:var(--navy);color:#fff}
  .label{font-weight:700;font-size:13px;letter-spacing:.06em;color:var(--teal);text-transform:uppercase}
  .panel--navy .label{color:var(--teal-light)}
  .body-copy{font-size:11px;line-height:1.45}
  .brand{font-family:"Source Serif 4",serif;font-weight:600;color:var(--navy);text-transform:uppercase;text-align:center;line-height:1.05;display:flex;flex-direction:column;align-items:center;gap:8px}
  .brand-mark{width:14px;height:14px;background:var(--navy)}
  .photo{position:absolute}
  .wave{position:absolute;left:0;bottom:0;width:100%}

  /* outside */
  .about{width:285px}
  .about > .label{position:absolute;left:28px;top:44px}
  .about-copy{position:absolute;left:28px;top:70px;width:225px}
  .serve{position:absolute;left:26px;top:200px;display:flex;gap:14px}
  .serve .label{margin-bottom:8px}
  .serve .body-copy{width:150px}
  .about .photo{left:0;top:320px;width:285px;height:120px;background:linear-gradient(180deg,#1e3a5e 0%,#4a5a6a 55%,#2b3a2c 100%)}

  .contact{width:303px}
  .contact .brand{position:absolute;left:0;right:0;top:42px;font-size:21px}
  .contact .rule{position:absolute;left:31px;top:202px;width:80px;height:1px;background:var(--teal)}
  .contact > .label{position:absolute;left:31px;top:220px}
  .contact-list{position:absolute;left:31px;top:254px;list-style:none;display:flex;flex-direction:column;gap:14px}
  .contact-list li{display:flex;align-items:flex-start;gap:10px;font-size:12px;line-height:1.45}
  .contact-list li span + span{padding-top:5px}
  .icon-dot{flex:none;width:28px;height:28px;border-radius:50%;background:var(--navy);display:flex;align-items:center;justify-content:center}

  .cover{width:498px}
  .cover .photo{right:0;top:0;width:300px;height:440px;background:linear-gradient(90deg,rgba(255,255,255,1) 0%,rgba(220,226,230,.6) 25%,#b9c3c8 55%,#8f9b8d 100%)}
  .cover .brand{position:absolute;left:20px;top:26px;width:160px;font-size:19px}
  .tagline{position:absolute;display:flex;align-items:center;gap:8px;font-size:11px;font-weight:700;letter-spacing:.12em;color:var(--teal)}
  .tagline::before,.tagline::after{content:"";width:38px;height:1px;background:var(--teal)}
  .cover .tagline{left:12px;top:150px}
  .headline{position:absolute;left:21px;top:176px;font-family:"Source Serif 4",serif;font-weight:600;font-size:41px;line-height:1.02;color:var(--navy);letter-spacing:-.01em}
  .accent{height:3px;width:62px;background:var(--orange)}
  .cover .accent{position:absolute;left:22px;top:316px}
  .cover .sub{position:absolute;left:22px;top:330px;width:200px;font-size:12.5px;line-height:1.35}

  /* inside */
  .service{width:348px}
  .service > .label{position:absolute;left:28px;top:28px}
  .service .short-rule{position:absolute;left:28px;top:53px;width:32px;height:2px;background:var(--teal)}
  .service .body-copy{position:absolute;left:28px;top:66px;width:225px}
  .service .photo{left:0;top:198px;width:348px;height:226px;background:linear-gradient(180deg,#6f6a62 0%,#cfc7ba 45%,#e5ddd0 100%)}
  .added{position:absolute;left:24px;top:325px;width:300px;height:79px;border-radius:12px;background:var(--navy);border:2px solid #fff;display:flex;align-items:center;gap:14px;padding:0 16px;color:#fff}
  .added svg{flex:none}
  .added .label{font-size:14px;color:var(--teal-light);margin-bottom:3px}
  .added p{font-size:12px;line-height:1.45}

  .details{width:350px}
  .detail{position:absolute;left:50px;display:flex;gap:17px}
  .ring{flex:none;width:48px;height:48px;border-radius:50%;border:2px solid #2aa3bd;display:flex;align-items:center;justify-content:center}
  .detail .label{font-size:14px;color:var(--teal-light);line-height:1.3}
  .schedule{top:34px}
  .schedule .short-rule{width:32px;height:2px;background:#2aa3bd;margin:6px 0 12px}
  .schedule p{font-size:13px;line-height:1.5}
  .schedule strong{font-weight:700}
  .divider{position:absolute;left:50px;top:140px;width:255px;height:1px;background:rgba(255,255,255,.3)}
  .benefits{top:162px;align-items:center}
  .checklist{position:absolute;left:70px;top:223px;list-style:none;display:flex;flex-direction:column;gap:9px}
  .checklist li{display:flex;gap:13px;font-size:13px;line-height:1.45}
  .tick{flex:none;width:14px;height:14px;border-radius:50%;background:var(--orange);margin-top:3px;display:flex;align-items:center;justify-content:center}

  .closing{width:388px;text-align:center}
  .closing h2{position:absolute;left:0;right:0;top:32px;font-family:"Source Serif 4",serif;font-weight:500;font-size:26px;line-height:1.04;color:var(--navy)}
  .closing .accent{position:absolute;left:163px;top:126px}
  .closing .cta{position:absolute;left:0;right:0;top:148px;font-size:18px;font-weight:700;color:var(--teal)}
  .closing .phone{position:absolute;left:0;right:0;top:178px;display:flex;justify-content:center;align-items:center;gap:10px;font-size:30px;font-weight:800;color:var(--navy)}
  .closing .phone .icon-dot{width:40px;height:40px}
  .closing .brand{position:absolute;left:0;right:0;top:252px;font-size:19px}
  .closing .tagline{left:0;right:0;top:340px;justify-content:center;font-size:10px}
  .closing .site{position:absolute;left:0;right:0;bottom:16px;font-size:12px;color:#fff;font-weight:600}
</style>
</head>
<body>

<section class="sheet sheet--outside">
  <div class="panel panel--navy about">
    <h3 class="label">About Us</h3>
    <p class="body-copy about-copy">Lanternway Hauling provides professional, reliable valet trash service for apartment communities and senior living properties. We handle the nightly collection so your residents can enjoy a cleaner, more convenient lifestyle.</p>
    <div class="serve">
      <svg width="44" height="46" viewBox="0 0 44 46" fill="none" stroke="#33b3cc" stroke-width="1.6"><rect x="4" y="14" width="16" height="30"/><rect x="20" y="4" width="18" height="40"/><path d="M8 20h3M13 20h3M8 27h3M13 27h3M8 34h3M13 34h3M24 10h3M31 10h3M24 18h3M31 18h3M24 26h3M31 26h3M24 34h3M31 34h3"/></svg>
      <div>
        <h3 class="label">Who We Serve</h3>
        <p class="body-copy">We partner with apartment communities, multifamily properties, and elder/ assisted living communities. Your residents are our priority.</p>
      </div>
    </div>
    <div class="photo" role="img" aria-label="Apartment complex at dusk with lit windows and landscaped walkway"></div>
  </div>

  <div class="panel contact">
    <div class="brand"><span class="brand-mark"></span>Lanternway<br>Hauling LLC</div>
    <div class="rule"></div>
    <h3 class="label">Contact Us</h3>
    <ul class="contact-list">
      <li><span class="icon-dot"><svg width="14" height="14" viewBox="0 0 24 24" fill="#fff"><path d="M6.6 10.8a15 15 0 0 0 6.6 6.6l2.2-2.2c.3-.3.7-.4 1-.2 1.1.4 2.3.6 3.6.6.6 0 1 .4 1 1V20c0 .6-.4 1-1 1A17 17 0 0 1 3 4c0-.6.4-1 1-1h3.5c.6 0 1 .4 1 1 0 1.3.2 2.5.6 3.6.1.3 0 .7-.2 1z"/></svg></span><span>555-314-7290</span></li>
      <li><span class="icon-dot"><svg width="14" height="12" viewBox="0 0 24 18" fill="none" stroke="#fff" stroke-width="2"><rect x="1" y="1" width="22" height="16" rx="2"/><path d="M1 2l11 8 11-8"/></svg></span><span>Marla@lanternway-hauling.example</span></li>
      <li><span class="icon-dot"><svg width="12" height="16" viewBox="0 0 24 32" fill="#fff"><path d="M12 0a12 12 0 0 0-12 12c0 9 12 20 12 20s12-11 12-20A12 12 0 0 0 12 0zm0 17a5 5 0 1 1 0-10 5 5 0 0 1 0 10z"/></svg></span><span>438 Quarry Ridge Road,<br>SUITE,<br>Millbrook, NJ 08000</span></li>
    </ul>
    <svg class="wave" height="40" viewBox="0 0 303 40" preserveAspectRatio="none"><path d="M0 22 Q150 2 303 6 V40 H0Z" fill="var(--orange)"/><path d="M0 28 Q150 6 303 10 V40 H0Z" fill="var(--teal-band)"/></svg>
  </div>

  <div class="panel cover">
    <div class="photo" role="img" aria-label="Branded dark trash can on a path beside an apartment building"></div>
    <div class="brand"><span class="brand-mark"></span>Lanternway<br>Hauling LLC</div>
    <div class="tagline">VALET TRASH SERVICE</div>
    <h1 class="headline">Convenient<br>Valet Trash<br>Service</h1>
    <div class="accent"></div>
    <p class="sub">Reliable doorstep collection for apartment communities and senior living properties.</p>
    <svg class="wave" height="50" viewBox="0 0 498 50" preserveAspectRatio="none"><path d="M0 40 Q150 28 330 8 L340 14 Q160 34 0 44Z" fill="var(--orange)"/><path d="M0 24 Q150 14 330 14 Q260 30 0 44Z" fill="var(--teal-band)"/><path d="M0 26 Q160 30 330 12 L340 14 Q200 40 0 50Z" fill="var(--navy)"/></svg>
  </div>
</section>

<section class="sheet sheet--inside">
  <div class="panel service">
    <h3 class="label">Our Service</h3>
    <div class="short-rule"></div>
    <p class="body-copy">We collect trash from tenants at your doorstep, so you don't have to.<br>Our team ensures a consistent, discreet, and dependable service every night. Elder and assisted living communities are also ideal partners—helping create cleaner, safer environments for residents and staff alike.</p>
    <div class="photo" role="img" aria-label="Bright apartment lobby with armchairs and potted plants"></div>
    <div class="added">
      <svg width="40" height="40" viewBox="0 0 40 40" fill="none" stroke="var(--orange)" stroke-width="2"><circle cx="20" cy="22" r="13"/><path d="M14 22l4 4 8-8M20 3v4M6 8l3 3M34 8l-3 3"/></svg>
      <div>
        <h3 class="label">Added Service</h3>
        <p>Morning check-ups to ensure<br>nothing is left out for pickup.</p>
      </div>
    </div>
  </div>

  <div class="panel panel--navy details">
    <div class="detail schedule">
      <span class="ring"><svg width="22" height="22" viewBox="0 0 24 24" fill="none" stroke="#fff" stroke-width="2"><rect x="3" y="5" width="18" height="16" rx="2"/><path d="M3 10h18M8 3v4M16 3v4M7 14h2M11 14h2M15 14h2M7 17h2M11 17h2"/></svg></span>
      <div>
        <h3 class="label">Service Schedule</h3>
        <div class="short-rule"></div>
        <p>Collection<br><strong>Sunday through Thursday</strong></p>
      </div>
    </div>
    <div class="divider"></div>
    <div class="detail benefits">
      <span class="ring"><svg width="22" height="22" viewBox="0 0 24 24" fill="#fff"><path d="M12 2l3 7 7 .6-5.3 4.7 1.6 7.2L12 17.8 5.7 21.5l1.6-7.2L2 9.6 9 9z"/></svg></span>
      <h3 class="label">Benefits for<br>Your Community</h3>
    </div>
    <ul class="checklist">
      <li><span class="tick"><svg width="8" height="8" viewBox="0 0 10 10" fill="none" stroke="#fff" stroke-width="2"><path d="M2 5l2 2 4-4"/></svg></span>Cleaner communities</li>
      <li><span class="tick"><svg width="8" height="8" viewBox="0 0 10 10" fill="none" stroke="#fff" stroke-width="2"><path d="M2 5l2 2 4-4"/></svg></span>Reliable nightly service</li>
      <li><span class="tick"><svg width="8" height="8" viewBox="0 0 10 10" fill="none" stroke="#fff" stroke-width="2"><path d="M2 5l2 2 4-4"/></svg></span>Resident convenience</li>
      <li><span class="tick"><svg width="8" height="8" viewBox="0 0 10 10" fill="none" stroke="#fff" stroke-width="2"><path d="M2 5l2 2 4-4"/></svg></span>Ideal for multifamily and<br>assisted living</li>
      <li><span class="tick"><svg width="8" height="8" viewBox="0 0 10 10" fill="none" stroke="#fff" stroke-width="2"><path d="M2 5l2 2 4-4"/></svg></span>Responsive customer care</li>
    </ul>
  </div>

  <div class="panel closing">
    <h2>Let us help keep<br>your community<br>clean and convenient.</h2>
    <div class="accent"></div>
    <p class="cta">Call today to learn more.</p>
    <p class="phone"><span class="icon-dot"><svg width="20" height="20" viewBox="0 0 24 24" fill="#fff"><path d="M6.6 10.8a15 15 0 0 0 6.6 6.6l2.2-2.2c.3-.3.7-.4 1-.2 1.1.4 2.3.6 3.6.6.6 0 1 .4 1 1V20c0 .6-.4 1-1 1A17 17 0 0 1 3 4c0-.6.4-1 1-1h3.5c.6 0 1 .4 1 1 0 1.3.2 2.5.6 3.6.1.3 0 .7-.2 1z"/></svg></span>555-314-7290</p>
    <div class="brand"><span class="brand-mark"></span>Lanternway<br>Hauling LLC</div>
    <div class="tagline">VALET TRASH SERVICE</div>
    <svg class="wave" height="62" viewBox="0 0 388 62" preserveAspectRatio="none"><path d="M0 30 Q200 28 388 0 V62 H0Z" fill="var(--teal-band)"/></svg>
    <p class="site">www.lanternway-hauling.example</p>
  </div>
</section>

</body>
</html>
```